Colin Ashbury Racing

I am a racehorse trainer and wish to produce a business card with my details and logo.
The stable colours are Royal blue and black.
The card would need my name and contact details.
Thanks, Colin.

Target Market(s)

Horse owners

Industry/Entity Type

Business

Font styles to use
Serif

Colors
0555a3

Requirements
Must have
• My name. Colour scheme of blue and black.
Nice to have
• Horse or jockey

```html
<!DOCTYPE html>
<html lang="en">
<head>
<meta charset="utf-8">
<title>Colin Ashbury Racing – Business Card</title>
<link rel="stylesheet" href="https://fonts.googleapis.com/css2?family=Exo:wght@400;700&display=swap">
<style>
  :root {
    --page-bg: #2b2b2b;
    --card-white: #ffffff;
    --royal-blue: #0555a3;
    --name-blue: #1f2fb8;
    --ink: #111111;
    --ink-soft: #2a2a2a;
    --field-haze: #f3efc9;
    --field-gold: #e9de7a;
    --field-green: #a7a63c;
    --field-deep: #6f7a2a;
  }
  * { margin: 0; padding: 0; box-sizing: border-box; }
  html, body {
    width: 1200px;
    height: 1116px;
    overflow: hidden;
    background: var(--page-bg);
  }
  .canvas {
    position: relative;
    width: 1200px;
    height: 1116px;
    display: flex;
    align-items: center;
    justify-content: center;
  }
  .business-card {
    position: relative;
    width: 1000px;
    height: 572px;
    background: var(--card-white);
    overflow: hidden;
    box-shadow: 0 12px 30px rgba(0,0,0,0.45);
  }
  .card-photo {
    position: absolute;
    inset: 0;
    background:
      radial-gradient(ellipse 28% 55% at 74% 42%, #f6f1e6 0%, rgba(246,241,230,0) 70%),
      radial-gradient(ellipse 45% 22% at 72% 62%, rgba(236,214,120,0.75) 0%, rgba(236,214,120,0) 80%),
      linear-gradient(180deg,
        var(--card-white) 0%,
        var(--card-white) 42%,
        var(--field-haze) 56%,
        var(--field-gold) 66%,
        var(--field-green) 82%,
        var(--field-deep) 100%);
  }
  .contact-block {
    position: absolute;
    left: 58px;
    top: 168px;
    font-family: "Exo", sans-serif;
  }
  .holder-name {
    font-weight: 400;
    font-size: 34px;
    color: var(--name-blue);
    letter-spacing: 0.5px;
    line-height: 1.1;
  }
  .holder-role {
    font-weight: 700;
    font-size: 32px;
    color: var(--ink);
    letter-spacing: 0.5px;
    line-height: 1.15;
  }
  .holder-phone {
    margin-top: 50px;
    font-weight: 400;
    font-size: 30px;
    color: var(--ink-soft);
    letter-spacing: 1px;
  }
  .holder-email {
    margin-top: 18px;
    font-weight: 400;
    font-size: 21px;
    color: var(--ink-soft);
    letter-spacing: 0.5px;
  }
</style>
</head>
<body>
  <main class="canvas">
    <section class="business-card">
      <div class="card-photo" role="img" aria-label="Photograph of a white horse rearing in a sunlit golden grass field, filling the right side and bottom of the card"></div>
      <div class="contact-block">
        <p class="holder-name">Colin Ashbury</p>
        <p class="holder-role">Racehorse trainer</p>
        <p class="holder-phone">(301) 555-0142</p>
        <p class="holder-email">colin@ashburyracing.com</p>
      </div>
    </section>
  </main>
</body>
</html>
```